・Webサイト作成サービス『ミモザ・サイトキット』内で、利用者が選択できるデザインテーマの新規作成依頼です。
・既存デザインとは異なる雰囲気のデザイン作成をお願いします。
・トップページのデザイン採用後、同テイストで一部下層ページのデザイン作成も依頼予定です

既存デザイン(サンプルサイトです)
https://sample.velorn.jp/

■サービス概要
・保険代理店向けのサブスクサービスです
・ノーコードでWebサイトを作成できます
・専用の管理画面から情報の追加や更新を行います
・Webサイトのデザインテーマも管理画面から選択します

サービスサイト
https://lp.velorn.jp/
・優しさを感じる「アットホーム」なデザインを希望します
・要素の角に丸みを持ったデザインとしてください
・色はブルー系で同系色にまとめてください
※ サービス移植後は基本色を変更し、12色での展開を予定しているため
・写真やバナー等の画像は既存サイトより保存して組み込んでください
※ 画像等はサービス共通のため、デザインいただく必要ありません
・表示内容は既存サイトを参考としてください
・CSSを変更するだけで対応可能な程度であれば多少のレイアウト変更はOKです
※ HTMLはそのままで、CSSを切り替えるだけでデザインを変える仕組みのため

■納品形式
Adobe XD での納品をお願いします。
https://sample.velorn.jp/
1ページ
青系
■納品形式
Adobe XD での納品をお願いします。
ページに表示するコンテンツの構成は変更できませんが、CSSで変更できる範囲で既存デザインとの違いを出したり、見た目の工夫をお願いします。

例えば...
・CSSの疑似要素を活用して見出しにあしらいを付ける
・背景へパターンを適用する
・お問い合わせボタンを絶対値で指定する
・既存のあしらい要素を非表示にする

さらに詳しく添付の画像に記載しておりますので、ご参照ください。
ご質問等あればお気軽にお願いします。

当該ランサーさんの初期の提案が、こちらの望んでいた雰囲気に一番近く、細かい部分にも丁寧な仕事ぶりが見られたことから、お声がけさせていただきました。
手直しの際もこちらの意図をしっかりと汲み取っていただき、少ない回数で望んだデザインへと至ることができました。

たくさんのご提案ありがとうございました。
また機会がございましたら、よろしくお願いいたします。

```html
<!DOCTYPE html>
<html lang="ja">
<head>
<meta charset="utf-8">
<title>サンプル保険サービス株式会社</title>
<link rel="stylesheet" href="https://fonts.googleapis.com/css2?family=Noto+Sans+JP:wght@400;500;700&family=Roboto:wght@400;500&display=swap">
<style>
:root{
  --blue:#3f8fd6;
  --blue-dark:#2a6fb3;
  --blue-pale:#e8f3fb;
  --blue-soft:#cfe4f5;
  --ink:#333;
  --muted:#777;
  --yellow:#ffdc32;
  --white:#fff;
  --gray:#b9b9b9;
  --line:#dfe6ec;
}
*{box-sizing:border-box;margin:0;padding:0}
html,body{width:1200px;height:2828px;overflow:hidden}
body{font-family:"Noto Sans JP",sans-serif;color:var(--ink);background:var(--white);position:relative}
.abs{position:absolute}
/* header */
.hero-photo{left:0;top:0;width:1200px;height:600px;background:linear-gradient(100deg,#e9f2e4 0%,#cfe3c9 25%,#b9cfe0 50%,#e8eef4 70%,#9cc5a4 100%)}
.site-header{left:0;top:0;width:1200px;height:64px;background:rgba(255,255,255,.92)}
.logo{left:160px;top:18px;font-size:22px;font-weight:500;color:var(--ink);display:flex;align-items:center;gap:10px}
.logo i{width:14px;height:14px;border-radius:50%;background:var(--blue);display:block}
.btn-contact{left:712px;top:10px;width:128px;height:44px;border-radius:22px;background:var(--yellow);font-size:16px;font-weight:700;display:flex;align-items:center;justify-content:center}
.tel-box{left:860px;top:8px;width:190px;height:48px;border:2px solid var(--blue);border-radius:12px;background:var(--white);text-align:center;color:var(--blue-dark)}
.tel-box b{display:block;font-family:Roboto,sans-serif;font-size:24px;font-weight:500;line-height:28px;margin-top:2px}
.tel-box small{font-size:10px;color:var(--muted)}
.gnav{left:180px;top:74px;width:860px;height:38px;border-radius:19px;background:rgba(63,143,214,.85);display:flex;justify-content:space-around;align-items:center;color:var(--white);font-size:15px}
.hero-copy{left:180px;top:290px;font-size:38px;font-weight:500;line-height:64px;color:var(--white);text-shadow:0 2px 6px rgba(0,0,0,.25)}
.hero-news{left:180px;top:528px;width:580px;height:56px;background:var(--white);border-radius:10px;display:flex;align-items:center;padding:0 20px;gap:14px;font-size:14px}
.tag{background:var(--blue);color:var(--white);font-size:11px;padding:2px 10px;border-radius:10px}
.date{font-family:Roboto,sans-serif;font-size:13px;color:var(--muted)}
/* intro cards */
.intro-band{left:0;top:600px;width:1200px;height:440px;background:repeating-linear-gradient(45deg,#f3f8fc 0 10px,#fff 10px 20px)}
.card{top:660px;width:272px;height:330px;background:var(--white);border-radius:16px;box-shadow:0 4px 14px rgba(42,111,179,.15);overflow:hidden}
.card .img{height:180px;background:linear-gradient(135deg,#bfe0a8,#e7f2d8)}
.card h3{font-size:16px;color:var(--blue-dark);margin:18px 18px 8px}
.card p{font-size:13px;line-height:22px;margin:0 18px;color:var(--muted)}
.card .arrow{position:absolute;right:16px;bottom:16px;width:28px;height:28px;border-radius:50%;background:var(--blue)}
/* section heads */
.sec-title{width:1200px;left:0;text-align:center;font-size:24px;font-weight:700;color:var(--blue-dark)}
.sec-sub{width:1200px;left:0;text-align:center;font-family:Roboto,sans-serif;font-size:11px;letter-spacing:2px;color:var(--muted)}
.sec-title::after{content:"";display:block;width:40px;height:3px;border-radius:2px;background:var(--blue);margin:8px auto 0}
/* online service */
.service-band{left:0;top:1060px;width:1200px;height:400px;background:var(--blue-pale)}
.svc{width:264px;height:104px;border:4px solid;border-radius:10px;background:var(--white);display:flex;align-items:center;justify-content:center;gap:14px;font-weight:700;font-size:22px;line-height:26px}
.svc i{width:44px;height:44px;border-radius:50%;display:block}
.svc small{display:block;font-size:18px}
/* news */
.news-title{left:180px;top:1500px;font-size:24px;font-weight:700;color:var(--blue-dark)}
.news-title::after{content:"";display:block;width:40px;height:3px;background:var(--blue);border-radius:2px;margin-top:8px}
.news-list{left:400px;top:1500px;width:632px}
.news-item{height:52px;border-bottom:1px solid var(--line);display:flex;align-items:center;gap:16px;font-size:14px}
.more{left:900px;top:1708px;font-size:13px;display:flex;align-items:center;gap:8px}
.more i{width:20px;height:20px;border-radius:50%;background:var(--blue);display:block}
/* links */
.link-banner{top:1936px;width:196px;height:76px;border:2px solid var(--line);border-radius:10px;background:var(--white);display:flex;align-items:center;justify-content:center;gap:8px;font-size:16px;font-weight:700;color:var(--blue-dark)}
.link-banner i{width:16px;height:16px;background:var(--blue);display:block}
/* contact */
.contact-band{left:0;top:2080px;width:1200px;height:180px;background:var(--blue-soft)}
.contact-tel{left:168px;top:2112px;width:424px;height:108px;background:var(--white);border-radius:54px;display:flex;align-items:center;gap:20px;padding-left:40px;color:var(--blue-dark)}
.contact-tel b{font-family:Roboto,sans-serif;font-size:40px;font-weight:500;display:block}
.contact-tel small{font-size:12px;color:var(--muted)}
.contact-mail{left:608px;top:2112px;width:424px;height:108px;background:var(--yellow);border-radius:54px;display:flex;align-items:center;justify-content:center;gap:20px;font-size:28px;font-weight:700}
/* footer */
.fnav{left:168px;top:2272px;width:864px;height:38px;border-radius:19px;background:var(--blue);display:flex;justify-content:space-around;align-items:center;color:var(--white);font-size:14px}
.f-company{left:168px;top:2350px;font-size:13px;line-height:22px}
.f-company strong{display:block;font-size:17px;margin-bottom:6px}
.f-text{left:500px;top:2350px;width:532px;font-size:12px;line-height:20px;color:var(--muted)}
.f-text li{list-style:none;margin-bottom:6px}
.banner{top:2572px;width:188px;height:80px;background:var(--gray);border-radius:8px;color:var(--white);display:flex;align-items:center;justify-content:center;font-size:20px;font-weight:700}
.f-links{left:168px;top:2712px;width:864px;display:flex;justify-content:space-between;font-size:12px;color:var(--muted)}
.copy{left:0;top:2764px;width:1200px;text-align:center;font-size:11px;color:var(--muted)}
</style>
</head>
<body>

<div class="abs hero-photo" role="img" aria-label="スーツ姿のスタッフが並ぶ明るい屋外写真"></div>
<header class="abs site-header">
  <div class="abs logo"><i></i>サンプル保険サービス株式会社</div>
  <a class="abs btn-contact">お問い合わせ</a>
  <div class="abs tel-box"><b>123-456-7890</b><small>平日9:00〜18:00</small></div>
</header>
<nav class="abs gnav"><span>ホーム</span><span>会社概要について</span><span>サービスのご案内</span><span>スタッフ紹介</span><span>お知らせ</span></nav>
<h1 class="abs hero-copy">お客さま一人ひとりに合った<br>保険を提案します</h1>
<div class="abs hero-news"><span class="date">2024.04.01</span><span class="tag">お知らせ</span><span>新型コロナウイルスの対応状況について</span></div>

<div class="abs intro-band"></div>
<article class="abs card" style="left:168px"><div class="img" role="img" aria-label="緑の木々に囲まれた建物の写真"></div><h3>当社について</h3><p>保険のプロとして、地域の皆さまの暮らしを安心で支えます。</p><span class="arrow"></span></article>
<article class="abs card" style="left:464px"><div class="img" role="img" aria-label="保険の資料を手にした相談の様子の写真" style="background:linear-gradient(135deg,#f4e3a8,#dbe9f5)"></div><h3>サービスのご案内</h3><p>お客さまの状況に合わせて最適な保険商品をご提案します。</p><span class="arrow"></span></article>
<article class="abs card" style="left:760px"><div class="img" role="img" aria-label="笑顔のスタッフの写真" style="background:linear-gradient(135deg,#c9d6e6,#eef2f6)"></div><h3>スタッフ紹介</h3><p>経験豊富なスタッフが親身になってサポートいたします。</p><span class="arrow"></span></article>

<div class="abs service-band"></div>
<h2 class="abs sec-title" style="top:1096px">オンラインサービス</h2>
<p class="abs sec-sub" style="top:1148px">ONLINE SERVICE</p>
<a class="abs svc" style="left:168px;top:1168px;border-color:#e85a8c;color:#e85a8c"><i style="background:#e85a8c"></i><span>サンプル<small>生命保険</small></span></a>
<a class="abs svc" style="left:468px;top:1168px;border-color:#b5192a;color:#b5192a"><i style="background:#b5192a"></i><span>サンプル<small>自動車保険</small></span></a>
<a class="abs svc" style="left:764px;top:1168px;border-color:#1d3f8f;color:#1d3f8f"><i style="background:#1d3f8f"></i><span>サンプル<small>自動車保険</small></span></a>
<a class="abs svc" style="left:168px;top:1288px;border-color:#f08a24;color:#f08a24"><i style="background:#f08a24"></i><span>サンプル<small>旅行保険</small></span></a>
<a class="abs svc" style="left:468px;top:1288px;border-color:#5aa03c;color:#5aa03c"><i style="background:#5aa03c"></i><span>サンプル<small>ゴルフ保険</small></span></a>

<h2 class="abs news-title">新着情報</h2>
<ul class="abs news-list">
  <li class="news-item"><span class="date">2024.04.01</span><span class="tag">お知らせ</span><span>GW期間中の営業日のお知らせ</span></li>
  <li class="news-item"><span class="date">2024.03.15</span><span class="tag">コラム</span><span>保険の見直しチェックのポイント</span></li>
  <li class="news-item"><span class="date">2024.03.01</span><span class="tag">お知らせ</span><span>ウェブでのご相談受付を開始しました</span></li>
  <li class="news-item"><span class="date">2024.02.10</span><span class="tag">お知らせ</span><span>新型コロナウイルスの対応状況について</span></li>
</ul>
<div class="abs more"><i></i>一覧を見る</div>

<h2 class="abs sec-title" style="top:1844px">関連リンク</h2>
<p class="abs sec-sub" style="top:1896px">LINK</p>
<a class="abs link-banner" style="left:168px"><i></i>サンプル損保</a>
<a class="abs link-banner" style="left:392px"><i></i>サンプル生命</a>
<a class="abs link-banner" style="left:612px"><i></i>SAMPLE生命</a>
<a class="abs link-banner" style="left:836px"><i></i>フォトシェア</a>

<div class="abs contact-band"></div>
<div class="abs contact-tel">
  <svg width="44" height="44" viewBox="0 0 24 24"><path fill="#3f8fd6" d="M6.6 10.8a15 15 0 0 0 6.6 6.6l2.2-2.2a1 1 0 0 1 1-.25 11.4 11.4 0 0 0 3.6.57 1 1 0 0 1 1 1V20a1 1 0 0 1-1 1A17 17 0 0 1 3 4a1 1 0 0 1 1-1h3.5a1 1 0 0 1 1 1c0 1.25.2 2.45.57 3.57a1 1 0 0 1-.25 1z"/></svg>
  <div><b>123-456-7890</b><small>平日9:00〜18:00（土日祝・休み）</small></div>
</div>
<a class="abs contact-mail">
  <svg width="44" height="34" viewBox="0 0 44 34"><rect x="2" y="2" width="40" height="30" rx="4" fill="none" stroke="#333" stroke-width="3"/><path d="M4 5l18 14 18-14" fill="none" stroke="#333" stroke-width="3"/></svg>お問い合わせ</a>

<nav class="abs fnav"><span>ホーム</span><span>会社概要について</span><span>サービスのご案内</span><span>スタッフ紹介</span><span>お知らせ</span></nav>
<div class="abs f-company"><small>保険代理店</small><strong>サンプル保険サービス株式会社</strong>〒000-0000<br>東京都中央区サンプル町1-2-3<br>TEL 123-456-7890<br>FAX 123-456-7891</div>
<ul class="abs f-text">
  <li>※ 当社は複数の保険会社と代理店契約を締結しており、取扱う商品は各社の商品となります。</li>
  <li>※ 保険契約の締結の媒介を行う代理店です。詳しくは各保険会社の資料をご確認ください。</li>
  <li>※ 掲載している内容は概要を説明したものです。ご契約の際は重要事項説明書を必ずお読みください。</li>
</ul>
<div class="abs banner" style="left:168px">バナー</div>
<div class="abs banner" style="left:392px">バナー</div>
<div class="abs banner" style="left:616px">バナー</div>
<div class="abs banner" style="left:844px">バナー</div>
<div class="abs f-links"><span>勧誘方針</span><span>個人情報保護方針</span><span>顧客本位の業務運営方針</span><span>反社会的勢力への対応</span><span>サイトマップ</span></div>
<p class="abs copy">© 2024 サンプル保険サービス株式会社 All Rights Reserved.</p>

</body>
</html>
```